VitaLern
Lifeline Instruction
Simple
Ted Marwick
Owner
287 Felcourt Lane Manahawkin, New Jersey 08050
Ted@VitaLern.com
www.VitaLern.com
Healthcare education and consulting.

```html
<!DOCTYPE html>
<html lang="en">
<head>
<meta charset="utf-8">
<title>VitaLern – Ted Marwick</title>
<link rel="stylesheet" href="https://fonts.googleapis.com/css2?family=Poppins:wght@400;500;600;700&display=swap">
<style>
  :root {
    --page: #ffffff;
    --card-top: #fbeee9;
    --card-bottom: #fdf6f3;
    --coral: #e0564b;
    --coral-deep: #b8372f;
    --ink: #4a1f1c;
    --rule: #a8463e;
  }
  * { margin: 0; padding: 0; box-sizing: border-box; }
  html, body {
    width: 1200px;
    height: 710px;
    overflow: hidden;
    background: var(--page);
    font-family: "Poppins", sans-serif;
  }
  .business-card {
    position: absolute;
    left: 269px;
    top: 168px;
    width: 662px;
    height: 380px;
    background: linear-gradient(160deg, var(--card-top), var(--card-bottom));
    color: var(--ink);
  }
  .bottom-band {
    position: absolute;
    left: 0; right: 0; bottom: 0;
    height: 14px;
    background: var(--coral);
  }
  .brand {
    position: absolute;
    left: 43px;
    top: 50px;
    display: flex;
    align-items: center;
    gap: 16px;
  }
  .brand-dot {
    width: 52px;
    height: 52px;
    border-radius: 50%;
    background: var(--coral);
  }
  .brand-name {
    font-size: 34px;
    font-weight: 500;
    line-height: 1;
    color: var(--coral-deep);
  }
  .brand-tagline {
    margin-top: 6px;
    font-size: 17px;
    font-weight: 400;
    color: var(--coral);
  }
  .person {
    position: absolute;
    right: 31px;
    top: 128px;
    text-align: right;
  }
  .person-name {
    font-size: 22px;
    font-weight: 700;
    color: var(--coral-deep);
    line-height: 1.2;
  }
  .person-role {
    font-size: 17px;
    font-weight: 600;
    color: var(--ink);
    line-height: 1.3;
  }
  .accent-bar {
    position: absolute;
    left: 638px;
    top: 125px;
    width: 15px;
    height: 72px;
    background: var(--coral);
  }
  .divider {
    position: absolute;
    left: 38px;
    top: 185px;
    width: 593px;
    height: 2px;
    background: var(--rule);
  }
  .contact-list {
    position: absolute;
    left: 46px;
    top: 220px;
    list-style: none;
  }
  .contact-list li {
    display: flex;
    align-items: center;
    gap: 12px;
    height: 31px;
    font-size: 13px;
    color: var(--ink);
  }
  .contact-icon { width: 17px; height: 17px; flex: none; }
  .address {
    position: absolute;
    left: 446px;
    top: 252px;
    font-size: 13px;
    font-style: normal;
    line-height: 31px;
    color: var(--ink);
  }
</style>
</head>
<body>
  <section class="business-card">
    <div class="brand">
      <div class="brand-dot"></div>
      <div>
        <div class="brand-name">VitaLern</div>
        <div class="brand-tagline">Lifeline Instruction</div>
      </div>
    </div>

    <div class="accent-bar"></div>
    <div class="person">
      <div class="person-name">Ted Marwick</div>
      <div class="person-role">Owner</div>
    </div>
    <div class="divider"></div>

    <ul class="contact-list">
      <li>
        <svg class="contact-icon" viewBox="0 0 20 20"><circle cx="10" cy="10" r="10" fill="#b8372f"/><path d="M7 5.5l1.6 2.2-1 1.1a6 6 0 0 0 3.6 3.6l1.1-1 2.2 1.6-.9 1.6c-3.8-.3-7.2-3.7-7.5-7.5z" fill="#fff"/></svg>
        <span>32-555-0147</span>
      </li>
      <li>
        <svg class="contact-icon" viewBox="0 0 20 20"><circle cx="10" cy="10" r="10" fill="#b8372f"/><rect x="7" y="4.5" width="6" height="11" rx="1" fill="#fff"/><rect x="8" y="6" width="4" height="7" fill="#b8372f"/></svg>
        <span>732-555-0186</span>
      </li>
      <li>
        <svg class="contact-icon" viewBox="0 0 20 20"><circle cx="10" cy="10" r="10" fill="#b8372f"/><path d="M5 9.5l10-4-3.5 10-2-4z" fill="#fff"/></svg>
        <span>Ted@VitaLern.com</span>
      </li>
      <li>
        <svg class="contact-icon" viewBox="0 0 20 20"><circle cx="10" cy="10" r="10" fill="#b8372f"/><rect x="5" y="6" width="10" height="8" rx="1" fill="none" stroke="#fff" stroke-width="1.5"/><line x1="5" y1="8.5" x2="15" y2="8.5" stroke="#fff" stroke-width="1.2"/></svg>
        <span>www.VitaLern.com</span>
      </li>
    </ul>

    <address class="address">
      287 Felcourt Lane<br>
      Larkhollow,<br>
      Vermont 05999
    </address>

    <div class="bottom-band"></div>
  </section>
</body>
</html>
```